cosmetic business needs inner and outer packaging

We, Velisto cosmetics, are a importer and oline retail of beauty products on an argan oil base. We will put 2 new products on the market.
A glass bottle 50ml of pure oil, and a 150g jar facemask.
Both need inner and outter packaging design.

Dimension of packaging:
Face mask jar:
- width : 20 cm - Height : 3 cm
Outter packaging:
- Width :  7,7 cm - height :  6,3 cm

Oil Bottle:
-Width : 10,4 cm - height : 4,3 cm
Outer packaging:
- Width :  3,8 cm - height :  12 cm

Pictures of the Jar & bottle are attached.

Our Brand:
Velisto design sources its products directly from the cooperatives in Morocco. The coorperatives are run by the local women. Therefore we support the local economy, independence of the woman and sustainable production.
We offer two classic beauty products. The pure argan oil, can be used for hair, skin or nails. It comes in a 50ml blue glass bottle.
A ghassoul face mask, comes in a jar of 150g.

For the design we envision a classicm, timeless design. Colours like lavendel, burgundy or indigo with specks of silver or gold. On the right side of the outter package we imagine an outline of what is inside. So a sillhouette of the jar/bottle.(see attached picture) But these are only ideas not limitations.
Attached some pictures of competitors.
If possible i would like to be able to amend the text as there cna be changes.

some competitors:
http://www.plumerin.co.uk/
http://www.kestrabow.co.uk/03_face_oil.html
https://orvinellu.com/

aldo obviously the logo has to be incoorperated in the packaging, so the bonus in the end will not demand any extra work

Target Market(s)

Taget marked:
Manily women, 26+ years, urban, interested in social and enviromental issues, earing money and able to spend on luxury products, interest in cosmetics,

Industry/Entity Type

Cosmetics

Logo Text

Velisto

Requirements
Must have
• amendable text on the back, as there are some legal requirements for cosmetic products.

```html
<!DOCTYPE html>
<html lang="en">
<head>
<meta charset="utf-8">
<title>Velisto Cosmetics – Charcoal Activated Face Mask Label</title>
<link href="https://fonts.googleapis.com/css2?family=Cinzel:wght@400&family=Josefin+Sans:wght@300;400&display=swap" rel="stylesheet">
<style>
  :root {
    --label-black: #0c0c0c;
    --silver: #d6d6d6;
    --silver-soft: #b9b9b9;
    --pill-grey: #3b3b3b;
    --ornament-tone: #9a9a9a;
    --bright: #eeeeee;
  }
  * { margin: 0; padding: 0; box-sizing: border-box; }
  html, body {
    width: 1200px;
    height: 1106px;
    overflow: hidden;
    background: var(--label-black);
  }
  .label {
    position: relative;
    width: 1200px;
    height: 1106px;
    background: var(--label-black);
    font-family: "Josefin Sans", sans-serif;
    color: var(--silver);
  }
  .label-frame { position: absolute; left: 0; top: 0; }
  .ornament {
    position: absolute;
    background: var(--ornament-tone);
    opacity: 0.55;
    border-radius: 6px;
  }
  .ornament--top { left: 584px; top: 400px; width: 36px; height: 44px; }
  .ornament--left { left: 384px; top: 504px; width: 52px; height: 32px; }
  .ornament--right { left: 764px; top: 504px; width: 52px; height: 32px; }
  .ornament--tag-left { left: 438px; top: 606px; width: 26px; height: 20px; }
  .ornament--tag-right { left: 742px; top: 606px; width: 26px; height: 20px; }
  .brand-name {
    position: absolute;
    left: 0;
    width: 1200px;
    text-align: center;
    font-family: "Cinzel", serif;
    font-weight: 400;
    color: var(--silver);
    line-height: 1;
    text-transform: uppercase;
  }
  .brand-name--primary { top: 462px; font-size: 56px; letter-spacing: 1px; }
  .brand-name--secondary { top: 522px; font-size: 46px; letter-spacing: 0; }
  .origin-tag {
    position: absolute;
    left: 462px;
    top: 592px;
    width: 284px;
    height: 48px;
    border: 2px solid var(--silver-soft);
    display: flex;
    align-items: center;
    justify-content: center;
    font-size: 21px;
    font-weight: 400;
    letter-spacing: 5px;
    padding-top: 4px;
  }
  .product-pill {
    position: absolute;
    left: 458px;
    top: 674px;
    width: 284px;
    height: 56px;
    border-radius: 28px;
    background: var(--pill-grey);
    display: flex;
    flex-direction: column;
    align-items: center;
    justify-content: center;
    font-size: 17px;
    line-height: 1.2;
    padding-top: 3px;
    text-transform: uppercase;
  }
  .claim {
    position: absolute;
    left: 0;
    width: 1200px;
    top: 744px;
    text-align: center;
    font-size: 40px;
    line-height: 1;
    font-weight: 400;
    letter-spacing: 1px;
    color: var(--bright);
  }
  .benefits {
    position: absolute;
    left: 0;
    width: 1200px;
    top: 796px;
    text-align: center;
    font-size: 10px;
    line-height: 1.25;
    letter-spacing: 0.5px;
    color: var(--silver-soft);
  }
  .net-weight {
    position: absolute;
    left: 0;
    width: 1200px;
    top: 834px;
    text-align: center;
    font-size: 22px;
    line-height: 1;
    letter-spacing: 2px;
    color: var(--bright);
  }
</style>
</head>
<body>
  <main class="label">
    <svg class="label-frame" width="1200" height="1106" viewBox="0 0 1200 1106" aria-hidden="true">
      <g fill="none" stroke="var(--silver-soft)" stroke-width="2">
        <polyline points="575,430 412,430 412,500"/>
        <polyline points="628,430 790,430 790,500"/>
        <line x1="412" y1="540" x2="412" y2="590"/>
        <line x1="790" y1="540" x2="790" y2="590"/>
        <line x1="412" y1="590" x2="436" y2="590"/>
        <line x1="766" y1="590" x2="790" y2="590"/>
        <rect x="593" y="574" width="12" height="12" transform="rotate(45 599 580)"/>
        <rect x="593" y="642" width="12" height="12" transform="rotate(45 599 648)"/>
      </g>
    </svg>

    <div class="ornament ornament--top" role="img" aria-label="Silver Moroccan filigree flourish above the frame"></div>
    <div class="ornament ornament--left" role="img" aria-label="Silver scroll flourish on the left side of the frame"></div>
    <div class="ornament ornament--right" role="img" aria-label="Silver scroll flourish on the right side of the frame"></div>
    <div class="ornament ornament--tag-left" role="img" aria-label="Small silver scroll beside the origin tag"></div>
    <div class="ornament ornament--tag-right" role="img" aria-label="Small silver scroll beside the origin tag"></div>

    <h1 class="brand-name brand-name--primary">Velisto</h1>
    <p class="brand-name brand-name--secondary">Cosmetics</p>

    <div class="origin-tag">MOROCCAN</div>

    <div class="product-pill">
      <span>Charcoal Activated</span>
      <span>Face Mask</span>
    </div>

    <p class="claim">100% Natural</p>

    <p class="benefits">For Facial Treatment, Minimizes Pores Reduces<br>Wrinkles, and Improves Overall Complexion</p>

    <p class="net-weight">150G</p>
  </main>
</body>
</html>
```